Attorney business card for two offices

Looking for a new business card design that can list both of my offices, one in Houston and one in West Texas. Want something masculine, easy to read, and conservative yet somewhat modern. Our current card has used a nautical star on it for years, but I am not necessarily attached to that. Also, a lot of our forms use dark green and orange. Second office address is P.O. Box 518, Mesa Vista, Texas 79617

```html
<!DOCTYPE html>
<html lang="en">
<head>
<meta charset="utf-8">
<title>The Barlow Law Firm – Business Card</title>
<link href="https://fonts.googleapis.com/css2?family=Raleway:wght@700;800&family=Lato:wght@400;700&family=Arimo:wght@400&display=swap" rel="stylesheet">
<style>
  :root{
    --bg:#a9a9a9;
    --green:#006600;
    --green-light:#0a7a0a;
    --orange:#e9a136;
    --ink:#3a3a3a;
    --rule:#8a8a8a;
    --white:#ffffff;
  }
  *{margin:0;padding:0;box-sizing:border-box}
  html,body{width:1200px;height:1200px;overflow:hidden}
  body{background:var(--bg);position:relative;font-family:"Arimo",Arial,sans-serif}

  .card{position:absolute;border-radius:16px;overflow:hidden;box-shadow:3px 4px 6px rgba(0,0,0,.45)}
  .card--back{left:203px;top:308px;width:364px;height:584px;background:var(--green)}
  .card--front{left:602px;top:307px;width:359px;height:587px;background:var(--white)}

  .back-texture{position:absolute;inset:0;background:linear-gradient(160deg,var(--green) 0%,var(--green-light) 55%,var(--green) 100%)}

  .firm-name{position:absolute;left:0;right:0;text-align:center;font-family:"Raleway",sans-serif;font-weight:800;font-variant:small-caps;letter-spacing:.3px;line-height:1;white-space:nowrap}
  .firm-tagline{position:absolute;display:flex;align-items:center;gap:6px;font-family:"Lato",sans-serif;font-weight:700;color:var(--orange);font-size:12px;letter-spacing:1.4px;line-height:1;white-space:nowrap}
  .firm-tagline::before,.firm-tagline::after{content:"";flex:1;height:1px;background:var(--orange)}

  .card--back .firm-name{top:506px;color:var(--white);font-size:22.5px}
  .card--back .firm-tagline{left:33px;right:33px;top:531px}

  .brand-mark{position:absolute;left:0;right:0;top:86px;display:flex;justify-content:center;align-items:center;gap:8px}
  .brand-mark__dot{width:16px;height:16px;border-radius:50%;background:var(--orange)}
  .brand-mark__name{font-family:"Raleway",sans-serif;font-weight:800;font-size:34px;color:var(--green);line-height:1}

  .card--front .firm-name{top:157px;color:var(--green);font-size:22px}
  .card--front .firm-tagline{left:34px;right:34px;top:181px}

  .person-name{position:absolute;left:0;right:0;top:259px;text-align:center;font-family:"Raleway",sans-serif;font-weight:800;font-variant:small-caps;font-size:23px;color:var(--green);line-height:1;white-space:nowrap}
  .person-title{position:absolute;left:0;right:0;top:288px;text-align:center;font-family:"Lato",sans-serif;color:var(--orange);font-size:15px;letter-spacing:.3px;line-height:1}

  .divider{position:absolute;left:0;right:0;display:flex;justify-content:center;align-items:center;gap:5px}
  .divider::before,.divider::after{content:"";width:36px;height:1px;background:var(--rule);margin:0 4px}
  .divider--contact{top:318px}
  .divider--address{top:446px}
  .divider--address::before,.divider--address::after{width:73px;margin:0 6px}
  .icon-box{width:25px;height:25px;border-radius:3px;background:var(--green);display:flex;align-items:center;justify-content:center}
  .icon-box svg{width:17px;height:17px}

  .contact-list,.address{position:absolute;left:0;right:0;text-align:center;color:var(--ink);font-size:17px;line-height:21.5px;letter-spacing:.2px;font-style:normal;white-space:nowrap}
  .contact-list{top:355px}
  .address--houston{top:478px}
  .address--west{top:526px}
</style>
</head>
<body>

<section class="card card--back">
  <div class="back-texture" role="img" aria-label="Subtle tone-on-tone star pattern across the green card back"></div>
  <h2 class="firm-name">The Barlow Law Firm. P.C.</h2>
  <p class="firm-tagline">ATTORNEYS AT LAW</p>
</section>

<section class="card card--front">
  <div class="brand-mark">
    <span class="brand-mark__dot"></span>
    <span class="brand-mark__name">Barlow Law</span>
  </div>
  <h1 class="firm-name">The Barlow Law Firm. P.C.</h1>
  <p class="firm-tagline">ATTORNEYS AT LAW</p>

  <p class="person-name">Daniel R. Barlow, Sr.</p>
  <p class="person-title">ATTORNEY AT LAW</p>

  <div class="divider divider--contact">
    <span class="icon-box" aria-label="Phone"><svg viewBox="0 0 24 24" fill="none" stroke="#fff" stroke-width="2"><path d="M3 9c0-3 4-4 9-4s9 1 9 4v2h-4V9H7v2H3z" fill="#fff"/><rect x="6" y="12" width="12" height="8" rx="1"/></svg></span>
    <span class="icon-box" aria-label="Fax"><svg viewBox="0 0 24 24" fill="none" stroke="#fff" stroke-width="2"><rect x="7" y="3" width="10" height="6"/><rect x="3" y="9" width="18" height="8" rx="1" fill="#fff"/><rect x="7" y="14" width="10" height="7" fill="#006600"/></svg></span>
    <span class="icon-box" aria-label="Email"><svg viewBox="0 0 24 24" fill="none" stroke="#fff" stroke-width="2"><rect x="3" y="6" width="18" height="12"/><path d="M3 6l9 7 9-7M3 18l7-6M21 18l-7-6"/></svg></span>
    <span class="icon-box" aria-label="Website"><svg viewBox="0 0 24 24" fill="none" stroke="#fff" stroke-width="2"><circle cx="12" cy="12" r="9"/><path d="M3 12h18M12 3c3 3 3 15 0 18M12 3c-3 3-3 15 0 18"/></svg></span>
  </div>

  <div class="contact-list">
    <p>(713) 555-0142</p>
    <p>(832) 555-0187</p>
    <p>Daniel@barlowtexlaw.com</p>
    <p>www.barlowtexlaw.com</p>
  </div>

  <div class="divider divider--address">
    <span class="icon-box" aria-label="Location"><svg viewBox="0 0 24 24"><path d="M12 2a7 7 0 0 0-7 7c0 5 7 13 7 13s7-8 7-13a7 7 0 0 0-7-7z" fill="#fff"/><circle cx="12" cy="9" r="2.6" fill="#006600"/></svg></span>
  </div>

  <address class="address address--houston">
    4410 Westcott Parkway, Suite 210<br>Houston, Texas 77055
  </address>
  <address class="address address--west">
    P.O. Box 518, Mesa Vista<br>Texas 79617
  </address>
</section>

</body>
</html>
```